Improving a camping website homepage header*

My client is very happy with his new website and its new functionalities. However, he's not very happy about the homepage design. Specifically, the header(this includes the menu, large header image and two columns beneath that). You can find the website here: http://lnkvo.example/siteTentra .

He forwarded me several other websites he likes. Which can be found in the attachments. I also included several pictures of the camping.

I'm looking for a design that will improve the header of the homepage with room for other global style chances. The logo cannot be changed.

Attachments
1) His old website homepage
2) Website mockup he liked.
3) Another website mockup he liked.

Other images can be found on the new website http://lnkvo.example/siteTentra or his old website http://lnkvo.example/formerSiteTentra.

Can you help us?
Updates

Hello guys. Here's a bit more information - Language used on the website is dutch. - The two columns left/right are supposed to link to Hire/Buy chalets. The client indicated that he finds these links important, but doesn't like the current design. I think this is partially the case because he doesn't like the icons. I'm looking forward to your designs!

Target Market(s)

30-50 year old wealthy people that want to purchase or rent cabins in the Netherlands.

Number of Pages Required

1 page

Colors

Designer to choose colors to be used in the design.

Requirements
Must have
• Improved header
Nice to have
• Global style changes
Should not have
• Logo changes

```html
<!DOCTYPE html>
<html lang="nl">
<head>
<meta charset="utf-8">
<title>Parc Lindewal</title>
<link href="https://fonts.googleapis.com/css2?family=Open+Sans:wght@400;600;700;800&display=swap" rel="stylesheet">
<style>
:root{
  --green:#4fa21e;
  --green-dark:#3e8615;
  --ink:#2b2b2b;
  --muted:#8a8a8a;
  --line:#e3e3e3;
  --soft:#f2f2f2;
  --dark:#1f2326;
  --darker:#15181a;
  --white:#ffffff;
}
*{box-sizing:border-box;margin:0;padding:0}
html,body{width:1200px;height:2524px;overflow:hidden}
body{font-family:"Open Sans",Arial,sans-serif;color:var(--ink);background:var(--white);font-size:14px}
.wrap{width:1080px;margin:0 auto;position:relative;height:100%}

/* nav */
.site-nav{height:88px;border-bottom:1px solid var(--line)}
.site-nav .wrap{display:flex;align-items:center;justify-content:space-between}
.brand{display:flex;align-items:center;gap:10px;font-weight:700;font-size:22px;color:var(--green)}
.brand-mark{width:22px;height:22px;border-radius:50%;background:var(--green)}
.menu{display:flex;gap:34px;font-size:13px;font-weight:600;margin-left:auto;margin-right:60px}
.menu a{color:var(--ink);text-decoration:none;padding:32px 0 30px;border-bottom:3px solid transparent}
.menu a.active{color:var(--green);border-color:var(--green)}
.btn{display:inline-block;background:var(--green);color:var(--white);font-size:12px;font-weight:600;padding:10px 26px;border-radius:2px;text-decoration:none}

/* hero */
.hero{height:520px;position:relative;color:var(--white)}
.hero-photo{position:absolute;inset:0;background:linear-gradient(180deg,#3a3226 0%,#2a2a22 45%,#1c1f1b 100%)}
.hero-shade{position:absolute;inset:0;background:linear-gradient(90deg,rgba(0,0,0,.55),rgba(0,0,0,.15))}
.hero-text{position:absolute;left:60px;top:140px;width:560px}
.badge{display:inline-block;background:var(--green);font-size:13px;font-weight:700;padding:4px 10px;margin-bottom:12px}
.hero h1{font-size:56px;font-weight:800;line-height:1;letter-spacing:1px}
.hero h1 span{color:var(--green)}
.hero p{font-size:14px;line-height:1.55;margin-top:16px;opacity:.9}
.hero-bar{position:absolute;left:0;right:0;bottom:0;height:90px;background:rgba(0,0,0,.55)}
.hero-bar .wrap{display:flex;align-items:center}
.arrows{display:flex;gap:6px}
.arrows span{width:30px;height:30px;background:var(--white);display:flex;align-items:center;justify-content:center}
.arrows span.dim{background:rgba(255,255,255,.2)}
.contact-item{display:flex;align-items:center;gap:14px;position:absolute}
.contact-item small{display:block;font-size:11px;color:#bbb}
.contact-item b{font-size:16px;font-weight:600}

/* services */
.services{height:282px;background:var(--soft);padding-top:58px}
.services .wrap{display:flex;gap:40px;height:auto}
.service-card{flex:1;background:var(--white);height:166px;display:flex;gap:26px;padding:32px 30px;box-shadow:0 1px 3px rgba(0,0,0,.06)}
.icon-box{width:90px;height:90px;background:var(--green);flex:none;display:flex;align-items:center;justify-content:center}
.service-card h3{font-size:15px;font-weight:700;margin-bottom:10px}
.service-card p{font-size:12px;line-height:1.6;color:var(--muted)}

/* section titles */
.section-head{display:flex;align-items:center;justify-content:space-between;margin-bottom:22px}
.section-head h2{font-size:30px;font-weight:800;color:var(--ink)}
.section-head h2 span{color:var(--green)}
.mini-arrows{display:flex;gap:4px}
.mini-arrows i{width:22px;height:22px;background:#bdbdbd;display:block}
.mini-arrows i.on{background:var(--green)}

/* chalets */
.chalets{height:490px;padding-top:44px}
.chalet-grid{display:flex;gap:30px}
.chalet{flex:1;border:1px solid var(--line);box-shadow:0 1px 4px rgba(0,0,0,.06);height:340px}
.chalet-photo{height:178px;position:relative;background:linear-gradient(180deg,#9cb7cf 0%,#7f8d6a 55%,#4f5a38 100%)}
.price{position:absolute;left:0;bottom:0;height:40px;width:100%;background:linear-gradient(0deg,rgba(0,0,0,.6),rgba(0,0,0,0));display:flex;align-items:center;justify-content:space-between;padding:0 12px;color:var(--white)}
.price b{font-size:22px;font-weight:700}
.price small{font-size:11px;font-weight:400}
.dots{display:flex;gap:5px}
.dots i{width:16px;height:16px;border-radius:50%;background:var(--green);display:block}
.chalet-body{padding:16px 16px}
.chalet-body h4{font-size:13px;font-weight:700;line-height:1.4;margin-bottom:10px}
.specs{display:flex;flex-wrap:wrap;gap:8px 18px;font-size:11px;color:var(--muted);margin-bottom:12px}
.specs span{display:flex;align-items:center;gap:6px}
.specs span::before{content:"";width:12px;height:9px;background:#f0a35c;display:block}

/* about */
.about{height:380px;position:relative;color:var(--white);text-align:center}
.about-photo{position:absolute;inset:0;background:linear-gradient(90deg,#2a2f2c,#3c3a30 50%,#22282a)}
.about-shade{position:absolute;inset:0;background:rgba(10,14,16,.55)}
.about-inner{position:relative;padding-top:76px;width:900px;margin:0 auto}
.about h2{font-size:30px;font-weight:800;margin-bottom:16px}
.about p{font-size:12px;line-height:1.7;margin-bottom:26px;opacity:.9}

/* testimonials */
.testimonials{height:400px;padding-top:42px}
.quote-grid{display:flex;gap:40px;padding:10px 0 0}
.quote{flex:1;display:flex;gap:22px}
.avatar{width:66px;height:66px;border-radius:50%;background:#c9c3bb;flex:none;margin-top:48px}
.quote-text{position:relative;padding-left:30px}
.quote-text::before{content:"\201C";position:absolute;left:0;top:-18px;font-size:64px;color:#cfcfcf;font-weight:700}
.quote-text p{font-size:12px;line-height:1.7;color:#555}
.quote-text b{display:block;font-size:12px;margin-top:10px}
.quote-text b span{font-weight:400;color:var(--muted)}
.pager{display:flex;justify-content:center;gap:8px;margin-top:70px}
.pager i{width:8px;height:8px;border-radius:50%;background:#c9c9c9;display:block}
.pager i.on{background:var(--green)}

/* footer */
.site-footer{height:316px;background:var(--dark);color:#cfcfcf;padding-top:40px}
.footer-cols{display:flex;gap:40px}
.footer-cols h5{color:var(--white);font-size:14px;font-weight:700;margin-bottom:16px}
.fcol{font-size:12px;line-height:2.15}
.fcol.contact{width:230px}
.fcol.contact div{display:flex;gap:10px;align-items:center}
.fcol.contact div::before{content:"";width:10px;height:10px;background:var(--green);border-radius:2px;flex:none}
.fcol.links{width:190px}
.fcol.links div::before{content:"\203A  ";color:var(--green)}
.thumbs{display:grid;grid-template-columns:repeat(2,110px);gap:10px;width:240px}
.thumbs div{height:72px;background:linear-gradient(180deg,#7c95a8,#58603f)}
.map{width:340px;height:210px;background:linear-gradient(135deg,#e7e4dc,#d6dccd)}
.bottom-bar{height:48px;background:var(--darker);color:#9a9a9a;font-size:11px}
.bottom-bar .wrap{display:flex;align-items:center;justify-content:space-between}
.social{display:flex;gap:6px}
.social i{width:24px;height:24px;background:#333a3e;display:block}
.social i.on{background:var(--green)}
</style>
</head>
<body>

<header class="site-nav">
  <div class="wrap">
    <div class="brand"><span class="brand-mark"></span>Parc Lindewal</div>
    <nav class="menu">
      <a class="active">Home</a><a>Huren</a><a>Financing</a><a>Chalets</a><a>Offers</a><a>Facilities</a><a>Contact</a>
    </nav>
    <a class="btn">Login</a>
  </div>
</header>

<section class="hero">
  <div class="hero-photo" role="img" aria-label="Wooden chalets among tall pine trees"></div>
  <div class="hero-shade"></div>
  <div class="hero-text">
    <span class="badge">RENT | BUY</span>
    <h1>PARC <span>LINDEWAL</span></h1>
    <p>Lorem ipsum dolor sit amet, consectetur adipiscing elit. Aenean commodo ligula eget dolor. Proin gravida dolor sit amet lacus accumsan et viverra justo commodo.</p>
  </div>
  <div class="hero-bar">
    <div class="wrap">
      <div class="arrows">
        <span class="dim"><svg width="10" height="10" viewBox="0 0 10 10"><path d="M7 1 3 5l4 4" stroke="#fff" stroke-width="2" fill="none"/></svg></span>
        <span><svg width="10" height="10" viewBox="0 0 10 10"><path d="M3 1l4 4-4 4" stroke="#333" stroke-width="2" fill="none"/></svg></span>
      </div>
      <div class="contact-item" style="left:330px">
        <svg width="22" height="22" viewBox="0 0 24 24"><path d="M6.6 10.8a15 15 0 0 0 6.6 6.6l2.2-2.2c.3-.3.7-.4 1-.2 1.1.4 2.3.6 3.6.6.6 0 1 .4 1 1V20c0 .6-.4 1-1 1A17 17 0 0 1 3 4c0-.6.4-1 1-1h3.5c.6 0 1 .4 1 1 0 1.3.2 2.5.6 3.6.1.3 0 .7-.2 1z" fill="var(--green)"/></svg>
        <div><small>Phone Number</small><b>0312 - 48 27 90</b></div>
      </div>
      <div class="contact-item" style="left:720px">
        <svg width="24" height="18" viewBox="0 0 24 18"><rect width="24" height="18" rx="2" fill="var(--green)"/><path d="M2 2l10 8 10-8" stroke="#fff" stroke-width="1.6" fill="none"/></svg>
        <div><small>Email Address</small><b>info@parclindewal.example</b></div>
      </div>
    </div>
  </div>
</section>

<section class="services">
  <div class="wrap">
    <div class="service-card">
      <div class="icon-box"><svg width="40" height="36" viewBox="0 0 40 36"><path d="M20 2 2 18h5v16h10V24h6v10h10V18h5z" fill="#fff"/></svg></div>
      <div><h3>RENT A CHALET</h3><p>Lorem ipsum dolor sit amet, consectetur adipiscing elit. Aenean commodo ligula eget dolor. Proin gravida dolor sit amet lacus accumsan et viverra justo commodo.</p></div>
    </div>
    <div class="service-card">
      <div class="icon-box"><svg width="44" height="30" viewBox="0 0 44 30"><rect x="1" y="1" width="42" height="28" rx="2" fill="none" stroke="#fff" stroke-width="3"/><circle cx="22" cy="15" r="7" fill="#fff"/></svg></div>
      <div><h3>BUY A CHALET</h3><p>Lorem ipsum dolor sit amet, consectetur adipiscing elit. Aenean commodo ligula eget dolor. Proin gravida dolor sit amet lacus accumsan et viverra justo commodo.</p></div>
    </div>
  </div>
</section>

<section class="chalets">
  <div class="wrap">
    <div class="section-head"><h2>RECENT <span>CHALETS</span></h2><div class="mini-arrows"><i></i><i class="on"></i></div></div>
    <div class="chalet-grid">
      <article class="chalet">
        <div class="chalet-photo" role="img" aria-label="Chalet with garden">
          <div class="price"><b>€ 350 <small>/Month</small></b><div class="dots"><i></i><i></i><i></i></div></div>
        </div>
        <div class="chalet-body">
          <h4>LOREM IPSUM DOLOR SIT AMET, CONSECTETUR ADIPISCING</h4>
          <div class="specs"><span>Bedroom (3)</span><span>Bathroom (2)</span><span>Area 1200 Sq</span><span>Garden 300 Sq</span></div>
          <a class="btn">Learn More</a>
        </div>
      </article>
      <article class="chalet">
        <div class="chalet-photo" role="img" aria-label="Chalet among trees">
          <div class="price"><b>€ 284 <small>/Month</small></b><div class="dots"><i></i><i></i><i></i></div></div>
        </div>
        <div class="chalet-body">
          <h4>LOREM IPSUM DOLOR SIT AMET, CONSECTETUR ADIPISCING</h4>
          <div class="specs"><span>Bedroom (2)</span><span>Bathroom (1)</span><span>Area 1000 Sq</span><span>Garden 250 Sq</span></div>
          <a class="btn">Learn More</a>
        </div>
      </article>
      <article class="chalet">
        <div class="chalet-photo" role="img" aria-label="Large wooden chalet">
          <div class="price"><b>€ 670 <small>/Month</small></b><div class="dots"><i></i><i></i><i></i></div></div>
        </div>
        <div class="chalet-body">
          <h4>LOREM IPSUM DOLOR SIT AMET, CONSECTETUR ADIPISCING</h4>
          <div class="specs"><span>Bedroom (4)</span><span>Bathroom (2)</span><span>Area 1500 Sq</span><span>Garden 400 Sq</span></div>
          <a class="btn">Learn More</a>
        </div>
      </article>
    </div>
  </div>
</section>

<section class="about">
  <div class="about-photo" role="img" aria-label="Wooden chalet front in the forest"></div>
  <div class="about-shade"></div>
  <div class="about-inner">
    <h2>KNOW ABOUT US</h2>
    <p>Lorem ipsum has been the industry's standard dummy text ever since the early days, when an unknown printer took a galley of type and scrambled it to make a type specimen book. It has survived not only five centuries, but also the leap into electronic typesetting, remaining essentially unchanged. It was popularised with the release of sheets containing Lorem Ipsum passages, and more recently with desktop publishing software including versions of Lorem Ipsum.</p>
    <a class="btn">Read More</a>
  </div>
</section>

<section class="testimonials">
  <div class="wrap">
    <div class="section-head"><h2>OUR <span>TESTIMONIALS</span></h2><div class="mini-arrows"><i></i><i class="on"></i></div></div>
    <div class="quote-grid">
      <div class="quote">
        <div class="avatar" role="img" aria-label="Guest portrait"></div>
        <div class="quote-text"><p>Lorem ipsum dolor sit amet, consectetur adipiscing elit. Aenean commodo ligula eget dolor. Proin gravida dolor sit amet lacus accumsan et viverra justo commodo. Proin sodales pulvinar tempor.</p><b>Jane Doe <span>/ CEO Company</span></b></div>
      </div>
      <div class="quote">
        <div class="avatar" role="img" aria-label="Guest portrait"></div>
        <div class="quote-text"><p>Lorem ipsum dolor sit amet, consectetur adipiscing elit. Aenean commodo ligula eget dolor. Proin gravida dolor sit amet lacus accumsan et viverra justo commodo. Proin sodales pulvinar tempor.</p><b>Jane Doe <span>/ CEO Company</span></b></div>
      </div>
    </div>
    <div class="pager"><i></i><i class="on"></i><i></i></div>
  </div>
</section>

<footer class="site-footer">
  <div class="wrap">
    <div class="footer-cols">
      <div class="fcol contact">
        <h5>Contact</h5>
        <div>Heideweg 12</div><div>4100 AA Voorstad</div><div>0312 - 48 27 90</div><div>0312 - 48 27 91</div><div>info@parclindewal.example</div><div>parclindewal.example</div>
      </div>
      <div class="fcol links">
        <h5>Site Map</h5>
        <div>Home</div><div>Huren</div><div>Financing</div><div>Chalets</div><div>Aanbiedingen</div><div>Facilities</div><div>Contact</div>
      </div>
      <div class="fcol">
        <h5>Nieuwe Chalets</h5>
        <div class="thumbs">
          <div role="img" aria-label="Chalet thumbnail"></div><div role="img" aria-label="Chalet thumbnail"></div>
          <div role="img" aria-label="Chalet thumbnail"></div><div role="img" aria-label="Chalet thumbnail"></div>
        </div>
      </div>
      <div class="fcol">
        <h5>Our Location</h5>
        <div class="map" role="img" aria-label="Map showing the park location"></div>
      </div>
    </div>
  </div>
</footer>

<div class="bottom-bar">
  <div class="wrap">
    <span>Copyright 2024 | Parc Lindewal</span>
    <div class="social"><i></i><i></i><i class="on"></i><i></i><i></i><i></i><i></i><i></i><i></i><i></i><i></i><i></i></div>
  </div>
</div>

</body>
</html>
```